Business Cards for Logistics Company

Looking to update Business Card Design.
Logo is attached. Blue background is not a part of the logo, you can remove it in layers.

Company: Harbor Crest Freightways
Industry: Logistics, Container Shipping

Address:
418 Willow Bend Ave
Bayonne NJ 07419

Phones:
p. 201-555-0143
f. 201-555-0178
c. very by person's name

Website: www.hcfroute.example

Design has to include person's name and position.
OLD Design is included.

B2B

Business

Card Size (non standard): 1039 x 697 pixels, 300dpi
Template is attached.

Font styles to use
Serif
Sans Serif

```html
<!DOCTYPE html>
<html lang="en">
<head>
<meta charset="utf-8">
<title>Harbor Crest Freightways – Business Card</title>
<link href="https://fonts.googleapis.com/css2?family=Open+Sans:ital,wght@0,400;0,600;0,700;1,400&family=Share+Tech+Mono&display=swap" rel="stylesheet">
<style>
  :root{
    --stage:#2c2c2e;
    --white:#ffffff;
    --ink:#3b3b45;
    --muted:#6a6a74;
    --brand:#2c3fa8;
    --brand-deep:#16237a;
    --navy:#1a2470;
    --navy-dark:#121a55;
    --sky:#1f8fd8;
    --sky-soft:#3aa7e6;
  }
  *{box-sizing:border-box;margin:0;padding:0}
  html,body{width:1200px;height:804px;overflow:hidden}
  body{
    background:var(--stage);
    font-family:"Open Sans",Arial,sans-serif;
    position:relative;
  }
  .card{
    position:absolute;
    top:228px;
    width:520px;
    height:349px;
    overflow:hidden;
    box-shadow:0 10px 30px rgba(0,0,0,.45);
  }

  /* Front */
  .card--front{left:50px;background:var(--white)}
  .front-band{
    position:absolute;left:0;top:0;bottom:0;width:92px;
    background:linear-gradient(180deg,var(--brand-deep) 0%,var(--brand) 45%,var(--sky) 100%);
  }
  .brand-square{
    position:absolute;left:40px;top:34px;width:78px;height:78px;
    background:var(--brand);
  }
  .wordmark{
    position:absolute;left:134px;top:40px;
    font-family:"Share Tech Mono",monospace;
    color:var(--ink);
    font-size:19px;letter-spacing:4px;line-height:1.25;
  }
  .wordmark span{display:block}
  .wordmark .line-two{padding-left:18px}
  .contact{
    position:absolute;left:134px;top:130px;
    font-size:12px;color:var(--muted);line-height:1.6;
  }
  .contact .company{color:var(--brand);font-weight:700;font-size:12.5px}
  .contact ul{list-style:none;margin-top:2px}
  .contact li{display:flex;align-items:center;gap:9px}
  .contact svg{width:11px;height:11px;flex:none;fill:var(--brand-deep)}
  .person{
    position:absolute;right:34px;top:150px;text-align:left;
  }
  .person .name{color:var(--brand);font-weight:700;font-size:20px}
  .person .role{color:var(--ink);font-size:14px;margin-left:66px}

  /* Back */
  .card--back{
    left:630px;
    background:radial-gradient(ellipse at 72% 40%,var(--navy) 0%,var(--navy-dark) 75%);
  }
  .world-map{
    position:absolute;right:0;top:0;width:330px;height:349px;
    background:radial-gradient(ellipse at 60% 55%,var(--sky-soft) 0%,var(--sky) 35%,rgba(31,143,216,.25) 65%,rgba(31,143,216,0) 85%);
  }
  .back-text{position:absolute;left:34px;top:96px;color:var(--white)}
  .back-wordmark{
    font-family:"Share Tech Mono",monospace;
    font-size:20px;letter-spacing:4px;line-height:1.3;
  }
  .back-wordmark span{display:block}
  .back-wordmark .line-two{padding-left:24px}
  .tagline{margin-top:26px;font-weight:700;font-size:13px}
  .services{font-style:italic;font-size:11px;margin-top:3px;opacity:.9}
  .rule{
    position:absolute;left:34px;top:288px;width:330px;height:1px;
    background:linear-gradient(90deg,rgba(255,255,255,.7),rgba(255,255,255,0));
  }
</style>
</head>
<body>

<section class="card card--front">
  <div class="front-band" role="img" aria-label="Blue band with faint world map"></div>
  <div class="brand-square"></div>
  <div class="wordmark"><span>HARBOR CREST</span><span class="line-two">FREIGHTWAYS</span></div>

  <div class="contact">
    <p class="company">Harbor Crest Freightways Inc</p>
    <p>418 Willow Bend Ave</p>
    <p>Bayonne NJ 07419</p>
    <ul>
      <li><svg viewBox="0 0 12 12"><path d="M2 1h2.5l1 3-1.5 1a6 6 0 0 0 3 3l1-1.5 3 1V11C5 11 1 7 1 2z"/></svg>201-555-0143</li>
      <li><svg viewBox="0 0 12 12"><path d="M3 0h6v12H3zM4 1v9h4V1z"/></svg>646-555-0192</li>
      <li><svg viewBox="0 0 12 12"><path d="M1 4h10v7H1zM3 1h6v3H3z"/></svg>201-555-0178</li>
      <li><svg viewBox="0 0 12 12"><path d="M1 2h10v8H1zM2 3l4 3 4-3v-.5H2z"/></svg>desk@hcfroute.example</li>
      <li><svg viewBox="0 0 12 12"><circle cx="6" cy="6" r="5"/></svg>www.hcfroute.example</li>
    </ul>
  </div>

  <div class="person">
    <p class="name">Daniel Marrow</p>
    <p class="role">General manager</p>
  </div>
</section>

<section class="card card--back">
  <div class="world-map" role="img" aria-label="World map in bright blue tones"></div>
  <div class="back-text">
    <div class="back-wordmark"><span>HARBOR CREST</span><span class="line-two">FREIGHTWAYS</span></div>
    <p class="tagline">International Transportation Solutions</p>
    <p class="services">Ocean &amp; Air Freight | Storage | Multimodal Transport</p>
  </div>
  <div class="rule"></div>
</section>

</body>
</html>
```